Tend Your Harvest - Keep your Bloom - The freedom to choose and participate in your own path to hea

I have a logo that needs to be turned into a large banner for my website. I want to keep the same font in the uploaded logo image. Now this image could stay at the top of the header kind of where it is now on the web site, It doesn't have to be the main thing on the page. I want this header to be artistic - alive, healthy, joyous - colorful banner that shows wellness, healing, vitality and hope.
If you had a chronic illness and came to my site what would you want to see? You'd want to feel empowered, enlightened, engaged, hopeful and feel the love, right?.
I look forward to getting your creative ideas and designs.

Target Market(s)

People struggling with illness who are looking for a better quality of life. We provide training and education on how to do that. Hope, happiness - healing - Vitality - whole natural foods - mediation - visualization - whole health.

Industry/Entity Type

Health And Wellness

Logo Text

Tend Your Harvest with the koru and with Marigold Thwaite (use the font on the uploaded file)

Requirements
Must have
• I've changed the photos in this order. You can pick up options here:
• https://www.filebarrow.example/s/x7pleqnrtwz2kdm/IMG_4402%20%20high%20resolution.jpg?dl=0
• https://www.filebarrow.example/s/m3bvohqyeuc8zta/IMG_4587%20high%20resolution.jpg?dl=0
• My original logo - Tend Your Harvest - Marigold Thwaite
• "Together we make tragic moments magic moments" Join us (sign up type button)
Nice to have
• Something stunningly simple, classy, inviting, where my message gets across.
• Here's a similar website to mine: http://dalvenhope.example
• I need a link to join up somewhere - with my quote.
• "My tragic moments have become magic moments" Join us (sign up type button)
Should not have
• I do not want other people in the header.
• No crunchy granola feel!
• This is gone mainstream now.

```html
<!DOCTYPE html>
<html lang="en">
<head>
<meta charset="utf-8">
<title>Tend Your Harvest — Header Banner</title>
<link rel="stylesheet" href="https://fonts.googleapis.com/css2?family=Quicksand:wght@500&family=Lobster&family=Lobster+Two:ital,wght@1,400&family=Luckiest+Guy&display=swap">
<style>
  :root {
    --teal: #1fc1b4;
    --teal-deep: #14a99d;
    --logo-teal: #3fb9c4;
    --navy: #1a1f3a;
    --sun: #f3e22a;
    --join-blue: #1b47c4;
    --white: #ffffff;
    --meadow-green: #8fd24a;
    --meadow-lime: #c6e86a;
    --meadow-gold: #e8c85a;
    --haze: #f6f7ee;
  }
  html, body {
    margin: 0;
    padding: 0;
    overflow: hidden;
  }
  .banner {
    position: relative;
    width: 1200px;
    height: 440px;
    overflow: hidden;
    background: var(--haze);
  }
  .meadow-backdrop {
    position: absolute;
    inset: 0;
    background:
      radial-gradient(ellipse 260px 220px at 110px 110px, rgba(255,255,255,0.95), rgba(255,255,255,0) 70%),
      radial-gradient(ellipse 320px 200px at 140px 400px, rgba(232,200,90,0.85), rgba(232,200,90,0) 75%),
      radial-gradient(ellipse 380px 260px at 560px 150px, rgba(143,210,74,0.9), rgba(143,210,74,0) 75%),
      radial-gradient(ellipse 420px 240px at 760px 360px, rgba(198,232,106,0.8), rgba(198,232,106,0) 75%),
      radial-gradient(ellipse 300px 260px at 980px 120px, rgba(220,236,150,0.7), rgba(220,236,150,0) 75%),
      linear-gradient(100deg, #f1f0d8 0%, #c9e27a 35%, #a5d85a 55%, #d6e79a 80%, #efe7d0 100%);
  }
  .portrait-area {
    position: absolute;
    right: 0;
    top: 0;
    width: 300px;
    height: 440px;
    background:
      radial-gradient(ellipse 90px 110px at 170px 80px, rgba(226,180,150,0.85), rgba(226,180,150,0) 75%),
      linear-gradient(180deg, rgba(238,220,200,0) 0%, rgba(150,215,225,0.75) 40%, rgba(120,200,215,0.9) 100%);
  }
  .brand {
    position: absolute;
    left: 26px;
    top: 14px;
    font-family: "Quicksand", sans-serif;
    font-weight: 500;
    color: var(--logo-teal);
    display: flex;
    align-items: center;
    gap: 10px;
  }
  .brand-dot {
    width: 22px;
    height: 22px;
    border-radius: 50%;
    background: var(--logo-teal);
    flex: none;
  }
  .brand-name {
    font-size: 22px;
    line-height: 1.2;
  }
  .quote-ribbon {
    position: absolute;
    left: 275px;
    top: 240px;
    width: 662px;
    height: 51px;
    background: var(--teal);
    display: flex;
    align-items: center;
    box-shadow: 0 2px 4px rgba(0,0,0,0.12);
  }
  .ribbon-mark {
    position: absolute;
    left: -4px;
    top: -4px;
    width: 59px;
    height: 59px;
    border-radius: 50%;
    background: var(--white);
    box-shadow: inset 0 0 0 10px var(--teal-deep);
  }
  .quote {
    margin-left: 72px;
    white-space: nowrap;
    display: flex;
    align-items: baseline;
  }
  .quote-lead {
    font-family: "Lobster Two", cursive;
    font-style: italic;
    font-size: 22px;
    color: var(--white);
    margin-right: 8px;
  }
  .quote-turn {
    font-family: "Lobster", cursive;
    font-size: 28px;
    color: var(--navy);
    margin-right: 4px;
  }
  .quote-magic {
    font-family: "Luckiest Guy", sans-serif;
    font-size: 31px;
    color: var(--sun);
    letter-spacing: 0.5px;
  }
  .join-button {
    position: absolute;
    left: 552px;
    top: 322px;
    width: 166px;
    height: 50px;
    text-decoration: none;
  }
  .join-button svg {
    position: absolute;
    inset: 0;
  }
  .join-label {
    position: absolute;
    left: 18px;
    top: 7px;
    font-family: "Lobster", cursive;
    font-size: 27px;
    color: var(--white);
  }
</style>
</head>
<body>
  <header class="banner">
    <div class="meadow-backdrop" role="img" aria-label="Soft out-of-focus spring meadow with green and golden bokeh light"></div>
    <div class="portrait-area" role="img" aria-label="Photo of the founder in a light turquoise shirt, seated and smiling"></div>

    <div class="brand">
      <span class="brand-dot"></span>
      <div class="brand-name">Tend Your Harvest<br>Marigold Thwaite</div>
    </div>

    <div class="quote-ribbon">
      <span class="ribbon-mark"></span>
      <p class="quote">
        <span class="quote-lead">My tragic moments</span>
        <span class="quote-turn">have become</span>
        <span class="quote-magic">MAGIC MOMENTS</span>
      </p>
    </div>

    <a class="join-button" href="#join">
      <svg width="166" height="50" viewBox="0 0 166 50" aria-hidden="true">
        <polygon points="0,0 166,0 148,25 166,50 0,50" fill="var(--join-blue)"/>
      </svg>
      <span class="join-label">Join us!</span>
    </a>
  </header>
</body>
</html>
```